Harrowgate Estates Business Card for Apartment Buildings

Create business cards for resident managers who run apartment buildings. The audience is the public who are searching for apartment rentals, and current residents who live at the apartment building. Key design element will be incorporating the company logo, however, the logo cannot dominate. The building name and manager name are more important than the logo. Current business card design leaves little room for copy, so we may need to reduce the size on the current card to allow for more space for copy.

Target Market(s)

Adults 18-65 years of age, who are looking for an apartment rental, plus current residents who live at our apartment buildings.

Industry/Entity Type

Property Management

Contact Information for Business Card

A major design element will be use of the company logo. Important property and manager contact information must be part of the design. The size of the logo will need to be reduced to make room for building and manager contact copy.

Font styles to use
Sans Serif

Colors
3176b5
000000
959595
ffffff

Requirements
Must have
• 1) Incorporate the company logo.
• 2) Use the company colors (dark blue, black/grey, over white).
• 3) FEATURE THE BUILDING NAME
• 4) FEATURE THE MANAGER NAME
• 5) The company name is less important than BUILDING and MANAGER
• 6) Manager contact information
• **SEE ATTACHED CREATIVE BRIEF**
Nice to have
• 1) Back of card logo watermark
• 2) Ability to write notes on back of carfd
Should not have
• Avoid letting the company logo dominate the card, the building name and manager are more important than the company logo.

```html
<!DOCTYPE html>
<html lang="en">
<head>
<meta charset="utf-8">
<title>Harrowgate Estates – Business Card</title>
<link href="https://fonts.googleapis.com/css2?family=Open+Sans:wght@400;600;700;800&display=swap" rel="stylesheet">
<style>
  :root {
    --brand-blue: #1464a5;
    --ink: #222222;
    --grey: #959595;
    --dark-grey: #444444;
    --paper: #ffffff;
    --backdrop: #1f1f1f;
  }
  * { box-sizing: border-box; margin: 0; padding: 0; }
  html, body { width: 1200px; height: 953px; overflow: hidden; }
  body {
    background: var(--backdrop);
    font-family: "Open Sans", Arial, sans-serif;
    display: flex;
    flex-direction: column;
    align-items: center;
    justify-content: center;
    gap: 64px;
  }
  .card {
    position: relative;
    width: 620px;
    height: 354px;
    background: var(--paper);
    overflow: hidden;
  }

  /* Back of card */
  .card-back .brand-mini {
    position: absolute;
    left: 34px; top: 34px;
    display: flex; align-items: center; gap: 8px;
  }
  .brand-dot {
    flex: none;
    width: 20px; height: 20px; border-radius: 50%;
    background: var(--brand-blue);
  }
  .brand-mini .brand-name {
    color: var(--brand-blue);
    font-weight: 800;
    font-size: 15px;
    letter-spacing: .5px;
    text-transform: uppercase;
  }
  .notes-label {
    position: absolute;
    left: 34px; top: 76px;
    color: var(--brand-blue);
    font-weight: 700;
    font-size: 17px;
  }
  .note-lines {
    position: absolute;
    left: 34px; right: 34px; top: 96px;
  }
  .note-lines .line {
    border-bottom: 2px dotted var(--brand-blue);
    height: 24px;
  }
  .note-lines .line:first-child { margin-left: 120px; }

  /* Front of card */
  .card-front .company {
    position: absolute;
    left: 40px; top: 150px;
    width: 200px;
    display: flex; align-items: center; gap: 10px;
    color: var(--brand-blue);
    font-weight: 800;
    text-transform: uppercase;
    line-height: 1;
  }
  .company .company-main { font-size: 22px; letter-spacing: -.3px; display: block; }
  .company .company-sub { font-size: 10px; letter-spacing: 3.5px; display: block; margin-top: 4px; color: var(--dark-grey); }
  .divider {
    position: absolute;
    left: 262px; top: 100px;
    width: 2px; height: 170px;
    background: var(--ink);
  }
  .contact {
    position: absolute;
    left: 290px; top: 82px;
    color: var(--ink);
    font-size: 14px;
    line-height: 1.45;
  }
  .manager-name {
    color: var(--brand-blue);
    font-weight: 800;
    font-size: 26px;
    text-transform: uppercase;
    line-height: 1.1;
  }
  .manager-title { color: var(--dark-grey); font-size: 15px; margin-bottom: 10px; }
  .contact-row { display: flex; }
  .contact-row .label { width: 58px; font-weight: 700; }
</style>
</head>
<body>

  <section class="card card-back" aria-label="Back of business card">
    <div class="brand-mini">
      <span class="brand-dot" aria-hidden="true"></span>
      <span class="brand-name">Harrowgate Estates LLC</span>
    </div>
    <p class="notes-label">Write Notes:</p>
    <div class="note-lines" aria-hidden="true">
      <div class="line"></div><div class="line"></div><div class="line"></div>
      <div class="line"></div><div class="line"></div><div class="line"></div>
      <div class="line"></div><div class="line"></div><div class="line"></div>
      <div class="line"></div>
    </div>
  </section>

  <section class="card card-front" aria-label="Front of business card">
    <div class="company">
      <span class="brand-dot" aria-hidden="true"></span>
      <p>
        <span class="company-main">Harrowgate</span>
        <span class="company-sub">Estates LLC</span>
      </p>
    </div>
    <div class="divider" aria-hidden="true"></div>
    <div class="contact">
      <p class="manager-name">Dana Whitcombe</p>
      <p class="manager-title">Property Manager</p>
      <p>2750 Alder Ridge Road #B210</p>
      <p>Fresno, CA 93711</p>
      <p class="contact-row"><span class="label">Phone</span><span>:- 555-214-7730</span></p>
      <p class="contact-row"><span class="label">Fax</span><span>:- 555-214-7731</span></p>
      <p class="contact-row"><span class="label">Email</span><span>:- dana@harrowgateestates.us</span></p>
      <p class="contact-row"><span class="label">Web</span><span>:- www.harrowgateestates.us</span></p>
    </div>
  </section>

</body>
</html>
```